Website for PeakWave Functional Training

We would like to launch a website for our boutique gym, PeakWave Functional Training. We'd like the website to have a lot of lime green which is one of our colors in our logo. The website will have a description of our workouts, membership, free trial class and location information.

Target Market(s)

Fitness enthusiasts, health conscious people, target ages 20-65, people looking to get fit and healthy, people looking to lose weight

Industry/Entity Type

Gym

Coding

Coded - Design and coding required

Number of Pages Required

1 page

Font styles to use
Serif

Colors
9ccb3b
34a7d8

Requirements
Must have
• A lot of lime green to match our logo. Let the website be fun, eye catchy. Our phone number which is 555-014-7391 to be easily dialed directly from our website.
Nice to have
• We would like to include this verbiage:
• -The Most FUN 1 hour workout
• -Affordable personal training/group training
• -Individualized workout programs
• -FUN workouts delivering results
• -Turn ON fat burn-The Most FUN 1 hour workout
• -Turn ON fat burning "EPOC" after burn
• We want our website to be easily seen on smart phones, iPads, Androids
Should not have
• Font that is hard on the eyes

```html
<!DOCTYPE html>
<html lang="en">
<head>
<meta charset="utf-8">
<title>PeakWave Functional Training</title>
<link rel="stylesheet" href="https://fonts.googleapis.com/css2?family=Lato:wght@300;400;700;900&family=Roboto+Slab:wght@300;400&family=Open+Sans:wght@400;600;700&display=swap">
<style>
:root{
  --lime:#9ccb3b;
  --lime-card:#b3cc1c;
  --blue:#34a7d8;
  --blue-deep:#1c7fae;
  --teal:#7ecfd2;
  --purple:#5d4f8e;
  --orange:#f15a22;
  --orange-dark:#e04a16;
  --plum:#3b3449;
  --ink:#222;
  --grey:#7a7a7a;
  --light:#f3f3f4;
  --line:#e4e4e4;
  --footer:#141414;
}
*{box-sizing:border-box;margin:0;padding:0}
html,body{width:1200px;height:4688px;overflow:hidden;background:#fff}
body{font-family:"Open Sans",Arial,sans-serif;color:var(--ink);font-size:14px}
.page{width:1088px;margin:0 auto;position:relative}
a{color:inherit;text-decoration:none}

/* top bar */
.topbar{height:88px;display:flex;align-items:center;justify-content:space-between;font-size:11px;color:var(--grey)}
.topbar .info{display:flex;align-items:center;gap:6px;width:330px}
.topbar .info.right{justify-content:flex-end;gap:18px}
.topbar .info svg{flex:none}
.topbar .phone{color:var(--lime);font-weight:700}
.brand{display:flex;align-items:center;gap:10px}
.brand-dot{width:22px;height:22px;border-radius:50%;background:var(--lime)}
.brand-name{font-family:"Lato",sans-serif;font-weight:900;font-size:20px;color:var(--lime);line-height:1.05;text-align:center}

/* nav */
.nav{height:52px;border-top:1px solid var(--line);border-bottom:1px solid var(--line);display:flex;align-items:center;justify-content:flex-end;position:relative}
.nav ul{list-style:none;display:flex;gap:30px;position:absolute;left:50%;transform:translateX(-50%);font-size:13px;font-weight:600}
.nav li.active{color:var(--lime)}
.nav .tools{display:flex;align-items:center;gap:12px}
.nav .tools span{width:18px;height:18px;border-radius:50%;background:#ddd}

/* hero */
.hero{margin-top:6px;height:379px;position:relative;background:linear-gradient(110deg,#2d9bd0 0%,#52b7e0 45%,#2f8fc0 100%);color:#fff;padding:68px 0 0 124px}
.hero h1{font-family:"Lato",sans-serif;font-weight:900;font-size:60px;line-height:1}
.hero h2{font-family:"Roboto Slab",serif;font-weight:300;font-size:54px;line-height:1.15}
.hero p{font-size:18px;margin-top:6px;opacity:.95}
.btn-join{display:inline-block;margin-top:22px;background:#135f78;border:3px solid #4bd0c9;border-radius:30px;padding:10px 40px;font-size:18px;font-weight:600}

/* about */
.about{height:491px;display:flex}
.about-visual{width:547px;position:relative;background:linear-gradient(180deg,#2a2a2a,#0e0e0e)}
.about-band{height:131px;background:var(--lime);color:#fff;padding:34px 0 0 26px;font-family:"Lato",sans-serif;font-size:70px;font-weight:300;line-height:1}
.about-band b{font-weight:900}
.about-photo{position:absolute;left:0;right:0;top:131px;bottom:0}
.about-visual .fitness{position:absolute;left:26px;top:134px;font-family:"Roboto Slab",serif;font-weight:300;font-size:54px;color:#fff}
.about-list{flex:1;background:var(--light);position:relative;padding:72px 40px 0 56px}
.about-list::before{content:"";position:absolute;left:0;top:230px;border:14px solid transparent;border-left-color:var(--lime)}
.feature{display:flex;gap:14px;margin-bottom:48px}
.feature svg{flex:none}
.feature h3{font-size:13px;font-weight:700;color:#333;margin-bottom:4px;letter-spacing:.3px}
.feature p{font-size:12px;color:var(--grey);line-height:1.5;max-width:440px}

/* schedule */
.schedule{height:468px;position:relative;background:linear-gradient(180deg,#1d1d1d,#2c2c2c 60%,#121212)}
.schedule h2{position:absolute;left:88px;top:72px;color:#fff;font-family:"Lato",sans-serif;font-weight:900;font-size:24px}
.timetable{position:absolute;left:88px;top:140px;width:912px;height:313px;background:var(--orange);padding:40px 44px 0}
.days{display:flex;justify-content:space-between;margin-bottom:40px}
.days span{width:104px;height:34px;border:2px solid #fff;border-radius:20px;color:#fff;font-size:12px;display:flex;align-items:center;justify-content:center}
.days span.active{background:#fff;color:var(--ink)}
.session{height:44px;background:var(--orange-dark);border-radius:22px;display:flex;align-items:center;padding:0 10px 0 24px;margin-bottom:6px;color:#fff;font-size:13px}
.session span:nth-child(1){width:230px}
.session span:nth-child(2){width:260px}
.session span:nth-child(3){flex:1}
.session .join{background:#fff;color:var(--ink);border-radius:18px;padding:6px 18px;font-size:12px;font-weight:600;flex:none}

/* classes */
.classes{height:816px;position:relative;text-align:center}
.section-title{font-family:"Lato",sans-serif;font-weight:400;font-size:36px;color:#222}
.section-sub{font-size:13px;color:var(--grey);margin-top:4px}
.classes .section-title{padding-top:24px}
.class-grid{position:absolute;left:119px;top:144px;display:grid;grid-template-columns:repeat(3,272px);gap:22px 20px}
.class-card{height:272px;display:flex;flex-direction:column;text-align:left}
.class-photo{height:169px}
.class-info{flex:1;display:flex;color:#fff;padding:16px 14px}
.class-info h4{font-size:13px;font-weight:600;width:136px}
.class-info .when{border-left:1px solid rgba(255,255,255,.5);padding-left:12px;font-size:11px;font-weight:700;display:flex;gap:8px}
.class-info .when small{display:block;font-weight:400;margin-top:14px}
.c-purple{background:var(--purple)}
.c-teal{background:var(--teal)}
.c-lime{background:var(--lime-card)}
.view-all{position:absolute;left:0;right:0;top:752px;font-size:12px;color:var(--lime);font-weight:600}

/* gallery */
.gallery{height:550px;position:relative}
.gallery h2{position:absolute;left:88px;top:12px;font-family:"Lato",sans-serif;font-weight:900;font-size:24px}
.filters{position:absolute;right:88px;top:8px;display:flex;gap:10px}
.filters span{height:36px;padding:0 22px;border:2px solid var(--orange);border-radius:20px;display:flex;align-items:center;font-size:11px;font-weight:700;color:#444}
.filters span.active{background:var(--orange);color:#fff}
.gallery-grid{position:absolute;left:88px;top:72px;display:grid;grid-template-columns:repeat(3,304px);grid-template-rows:repeat(2,206px);gap:2px}

/* pricing */
.pricing{height:650px;background:var(--light);position:relative;text-align:center;padding-top:72px}
.plans{position:absolute;left:119px;top:206px;display:flex;gap:20px}
.plan{width:272px;height:375px;background:#fff;padding-top:40px}
.plan h3{font-family:"Lato",sans-serif;font-weight:400;font-size:20px}
.price{width:100px;height:100px;border-radius:50%;margin:18px auto 22px;color:#fff;display:flex;flex-direction:column;align-items:center;justify-content:center;font-family:"Lato",sans-serif;line-height:1}
.price .amount{display:flex;align-items:flex-start;font-size:40px;font-weight:300}
.price .amount sup{font-size:15px;margin-top:3px;margin-right:2px}
.price small{font-size:10px;margin-top:5px}
.plan ul{list-style:none;text-align:left;width:160px;margin:0 auto;font-size:12px;color:var(--grey)}
.plan li{display:flex;align-items:center;gap:8px;height:22px}
.plan li::before{content:"✓";color:var(--lime);font-weight:700}
.btn-plan{display:inline-block;margin-top:26px;background:var(--lime-card);color:#fff;font-size:11px;font-weight:700;padding:9px 18px}

/* appointment */
.appointment{height:469px;background:var(--plum);color:#fff;text-align:center;padding-top:62px;position:relative}
.appointment .section-title{color:#fff}
.appointment .section-sub{color:#cfcadb}
.form{position:absolute;left:263px;top:206px;width:562px;display:grid;grid-template-columns:272px 272px;gap:18px;text-align:left}
.field{height:44px;background:#fff;color:#999;font-size:12px;padding:12px 10px;border-radius:2px}
.field b{color:#333}
.field.tall{grid-row:span 2;height:106px}
.btn-send{position:absolute;left:535px;top:352px;background:var(--lime-card);color:#fff;font-size:12px;font-weight:700;padding:13px 26px}

/* promo */
.promo{height:344px;background:linear-gradient(90deg,#2b2423,#463833 50%,#2a2221);color:#fff;padding:56px 0 0 320px}
.promo h3{font-family:"Lato",sans-serif;font-weight:900;font-size:30px;letter-spacing:.5px}
.promo p{font-family:"Roboto Slab",serif;font-weight:300;font-size:32px;line-height:1.25;margin-top:18px}
.promo p em{font-style:normal;color:var(--orange);font-weight:400}
.btn-member{display:inline-block;margin-top:22px;border:2px solid var(--lime);border-radius:26px;padding:10px 40px;font-size:14px}

/* footer */
.footer{height:337px;background:var(--footer);color:#bbb;display:grid;grid-template-columns:237px 237px 237px 237px;padding:48px 0 0 56px}
.footer h4{color:#fff;font-size:15px;font-weight:700;margin-bottom:16px}
.footer p{font-size:12px;line-height:1.6;max-width:200px}
.socials{display:flex;gap:6px;margin-top:18px}
.socials span{width:16px;height:16px;border-radius:50%;background:var(--orange)}
.tweet{display:flex;gap:10px;font-size:12px;line-height:1.5}
.tweet .av{width:24px;height:24px;border-radius:50%;background:var(--lime);flex:none}
.tweet a{color:var(--lime)}
.photos{display:grid;grid-template-columns:repeat(3,56px);gap:6px}
.photos span{height:50px;background:linear-gradient(135deg,#6b5a48,#3a3430)}
.office li{list-style:none;display:flex;gap:10px;font-size:12px;margin-bottom:12px}
.office li::before{content:"";width:10px;height:10px;background:var(--orange);border-radius:2px;margin-top:3px;flex:none}
.copyright{height:38px;background:#0a0a0a;color:#777;font-size:11px;display:flex;align-items:center;justify-content:center;position:relative}
.to-top{position:absolute;right:16px;top:8px;width:22px;height:22px;background:var(--orange)}
</style>
</head>
<body>
<div class="page">

  <header class="topbar">
    <div class="info">
      <svg width="10" height="14" viewBox="0 0 10 14"><path d="M5 0a5 5 0 0 0-5 5c0 4 5 9 5 9s5-5 5-9a5 5 0 0 0-5-5zm0 7a2 2 0 1 1 0-4 2 2 0 0 1 0 4z" fill="#9ccb3b"/></svg>
      <span>48 Harbor Lane, Springvale</span>
    </div>
    <a class="brand" href="#">
      <span class="brand-dot"></span>
      <span class="brand-name">PeakWave<br>Functional Training</span>
    </a>
    <div class="info right">
      <span>Mo-Fr: 6am - 9pm / St-Su: 8am - 4pm</span>
      <a class="phone" href="tel:5550147391">555-014-7391</a>
    </div>
  </header>

  <nav class="nav">
    <ul>
      <li class="active">Home</li><li>Features</li><li>Classes</li><li>Schedule</li><li>About Us</li><li>Contact Us</li>
    </ul>
    <div class="tools">
      <svg width="14" height="14" viewBox="0 0 14 14"><circle cx="6" cy="6" r="4.5" fill="none" stroke="#444" stroke-width="1.6"/><path d="M9.5 9.5 13 13" stroke="#444" stroke-width="1.6"/></svg>
      <span></span><span></span>
    </div>
  </nav>

  <section class="hero" role="img" aria-label="Blue-toned photo of a gym workout behind the headline">
    <h1>The Most FUN</h1>
    <h2>1 hour workout</h2>
    <p>Ready to change your physique, but can't work out in the gym?</p>
    <a class="btn-join" href="#">Join with us</a>
  </section>

  <section class="about">
    <div class="about-visual">
      <div class="about-band">All <b>About</b></div>
      <div class="about-photo" role="img" aria-label="Dark photo of a muscular athlete"></div>
      <div class="fitness">Fitness</div>
    </div>
    <div class="about-list">
      <div class="feature">
        <svg width="22" height="16" viewBox="0 0 22 16"><path d="M2 8h18M4 3v10M18 3v10M7 5v6M15 5v6" stroke="#9ccb3b" stroke-width="2.5"/></svg>
        <div><h3>WEIGHT LIFTING</h3><p>Sed ut perspiciatis unde omnis iste natus error sit voluptatem accusantium doloremque laudantium, totam rem aperiam, eaque ipsa quae ab illo inventore veritatis.</p></div>
      </div>
      <div class="feature">
        <svg width="22" height="16" viewBox="0 0 22 16"><path d="M2 14 4 4l5 5 2-7 2 7 5-5 2 10z" fill="#9ccb3b"/></svg>
        <div><h3>BOUTIQUE</h3><p>Sed ut perspiciatis unde omnis iste natus error sit voluptatem accusantium doloremque laudantium, totam rem aperiam, eaque ipsa quae ab illo inventore veritatis.</p></div>
      </div>
      <div class="feature">
        <svg width="22" height="16" viewBox="0 0 22 16"><path d="M11 1 20 15H2z" fill="#9ccb3b"/></svg>
        <div><h3>YOGA</h3><p>Sed ut perspiciatis unde omnis iste natus error sit voluptatem accusantium doloremque laudantium.</p></div>
      </div>
    </div>
  </section>

  <section class="schedule" aria-label="Class schedule">
    <h2>CLASS SCHEDULE</h2>
    <div class="timetable">
      <div class="days">
        <span class="active">Monday</span><span>Tuesday</span><span>Wednesday</span><span>Thursday</span><span>Friday</span><span>Saturday</span><span>Sunday</span>
      </div>
      <div class="session"><span>Running</span><span>12:00pm - 12:00pm</span><span>Sam Rivera</span><a class="join" href="#">Join Now!</a></div>
      <div class="session"><span>Karate</span><span>12:00pm - 12:00pm</span><span>Lena Park</span><a class="join" href="#">Join Now!</a></div>
      <div class="session"><span>Body Building</span><span>1:30pm - 1:30pm</span><span>Joel Tanner</span><a class="join" href="#">Join Now!</a></div>
    </div>
  </section>

  <section class="classes">
    <h2 class="section-title">Our Classes</h2>
    <p class="section-sub">Choose Your Level and Pursue</p>
    <div class="class-grid">
      <article class="class-card"><div class="class-photo" role="img" aria-label="Photo of a yoga stretch" style="background:linear-gradient(135deg,#e9e4de,#b8ada3)"></div><div class="class-info c-purple"><h4>FlowStudio Barre</h4><div class="when"><span>▦</span><div>TUE, THU, SAT<small>10pm - 11pm</small></div></div></div></article>
      <article class="class-card"><div class="class-photo" role="img" aria-label="Photo of a group fitness class" style="background:linear-gradient(135deg,#d7c2b5,#8c7a72)"></div><div class="class-info c-teal"><h4>FlowStudio Restore</h4><div class="when"><span>▦</span><div>MON, WED, FRI<small>10pm - 11pm</small></div></div></div></article>
      <article class="class-card"><div class="class-photo" role="img" aria-label="Photo of a rolled yoga mat in sunlight" style="background:linear-gradient(135deg,#f2d39a,#6fa6a0)"></div><div class="class-info c-lime"><h4>FlowStudio Core</h4><div class="when"><span>▦</span><div>TUE, THU, SAT<small>10pm - 11pm</small></div></div></div></article>
      <article class="class-card"><div class="class-photo" role="img" aria-label="Photo of smiling class members" style="background:linear-gradient(135deg,#ead9cd,#b48f7a)"></div><div class="class-info c-purple"><h4>FlowStudio Restore</h4><div class="when"><span>▦</span><div>TUE, THU, SAT<small>10pm - 11pm</small></div></div></div></article>
      <article class="class-card"><div class="class-photo" role="img" aria-label="Photo of a stretch on the beach" style="background:linear-gradient(135deg,#9fd3e0,#5f9a7c)"></div><div class="class-info c-teal"><h4>FlowStudio Core</h4><div class="when"><span>▦</span><div>MON, WED, FRI<small>10pm - 11pm</small></div></div></div></article>
      <article class="class-card"><div class="class-photo" role="img" aria-label="Photo of a floor exercise" style="background:linear-gradient(135deg,#f0e0dc,#c48a8f)"></div><div class="class-info c-lime"><h4>FlowStudio Barre</h4><div class="when"><span>▦</span><div>MON, WED, FRI<small>10pm - 11pm</small></div></div></div></article>
    </div>
    <a class="view-all" href="#">View All Classes ➜</a>
  </section>

  <section class="gallery">
    <h2>OUR GALLERY</h2>
    <div class="filters"><span class="active">ALL</span><span>YOGA</span><span>FITNESS</span><span>GYM</span><span>RUNNING</span></div>
    <div class="gallery-grid">
      <div role="img" aria-label="Photo of a group aerobics session" style="background:linear-gradient(135deg,#c9b7a6,#6f5d50)"></div>
      <div role="img" aria-label="Photo of a step class" style="background:linear-gradient(135deg,#5f8f83,#2f4a44)"></div>
      <div role="img" aria-label="Photo of a seated stretch" style="background:linear-gradient(135deg,#e2d2c2,#a88e78)"></div>
      <div role="img" aria-label="Photo of dumbbell training" style="background:linear-gradient(135deg,#b3b8b0,#5d625a)"></div>
      <div role="img" aria-label="Photo of a lunge workout" style="background:linear-gradient(135deg,#d5d5d8,#7a7580)"></div>
      <div role="img" aria-label="Photo of a weight lifting session" style="background:linear-gradient(135deg,#6a6a6a,#262626)"></div>
    </div>
  </section>

  <section class="pricing">
    <h2 class="section-title">Simple Pricing</h2>
    <p class="section-sub">Start Yoga Practice Today</p>
    <div class="plans">
      <div class="plan"><h3>Regular Plan</h3><div class="price" style="background:var(--teal)"><span class="amount"><sup>$</sup>45</span><small>/ month</small></div><ul><li>Basic Yoga</li><li>Free Snacks</li><li>Flexible Timing</li><li>Certificate</li></ul><a class="btn-plan" href="#">Choose this Plan</a></div>
      <div class="plan"><h3>Silver Plan</h3><div class="price" style="background:var(--purple)"><span class="amount"><sup>$</sup>65</span><small>/ month</small></div><ul><li>Advanced Yoga</li><li>Free Snacks</li><li>Flexible Timing</li><li>Personal Attention</li></ul><a class="btn-plan" href="#">Choose this Plan</a></div>
      <div class="plan"><h3>Premium Plan</h3><div class="price" style="background:var(--lime-card)"><span class="amount"><sup>$</sup>75</span><small>/ month</small></div><ul><li>Deep Yoga Poses</li><li>Free Meditation</li><li>Free Snacks/Pilat</li><li>Kundalini Yoga</li></ul><a class="btn-plan" href="#">Choose this Plan</a></div>
    </div>
  </section>

  <section class="appointment">
    <h2 class="section-title">Make an Appointment</h2>
    <p class="section-sub">Start Yoga Practice Today</p>
    <div class="form">
      <div class="field"><b>Name<sup>*</sup></b> Name</div>
      <div class="field tall"><b>Message<sup>*</sup></b> Message</div>
      <div class="field"><b>Phone<sup>*</sup></b> Phone</div>
    </div>
    <a class="btn-send" href="#">Send Message</a>
  </section>

  <section class="promo" role="img" aria-label="Dark photo of an athlete training, behind the discount offer">
    <h3>FUN WORKOUTS DELIVERING RESULTS</h3>
    <p>PAY NOW AND<br>GET <em>35%</em> DISCOUNT</p>
    <a class="btn-member" href="#">Become a member</a>
  </section>

  <footer class="footer">
    <div>
      <h4>About Company</h4>
      <p>Train smart with friendly coaches, small groups and plans built for you. Every session is fun, focused and made to deliver results you can feel each week.</p>
      <div class="socials"><span></span><span></span><span></span><span></span><span></span><span></span></div>
    </div>
    <div>
      <h4>Follow Us Online</h4>
      <div class="tweet"><span class="av"></span><p>PeakWave<br>Fitness and boutique<br>PeakWave - Affordable personal training <a href="#">peakwave.fit/trial</a></p></div>
    </div>
    <div>
      <h4>Photo Stream</h4>
      <div class="photos"><span></span><span></span><span></span><span></span><span></span><span></span></div>
    </div>
    <div>
      <h4>Corporate Office</h4>
      <ul class="office">
        <li>48 Harbor Lane, Springvale</li>
        <li><a href="tel:5550147391">555-014-7391</a></li>
        <li>info@peakwave.fit</li>
        <li><a href="tel:5550147391">555-014-7391</a></li>
      </ul>
    </div>
  </footer>
  <div class="copyright">© Copyright PeakWave 2016. All Right Reserved<span class="to-top"></span></div>

</div>
</body>
</html>
```